Smartphone speedcam App design

We are Dubai based company named QWRN. We are looking design for our Android app. We developed Speed Camera intimation Android app. Our application required GPS/3G to run. The idea is to control over speeding and intimate users the speed camera nearby you.
You can use app while driving. App will intimate you if you crossed road speed limit. App also intimate when speed camera nearby you. For example, Speed camera after 500 meters , 400 meters...etc.

Target Market(s)

UAE market

Industry/Entity Type

It Company

Number of Pages Required

2 page

Requirements
Must have
• my app has option to intimate for speed camera. camera icon/image can appear while intimation only rest of design can show road speed and current driving speed.
• I have attached sample main screen for designer understanding.
Nice to have
• designers can search related apps

```html
<!DOCTYPE html>
<html lang="en">
<head>
<meta charset="utf-8">
<title>QWRN Speed Limit</title>
<link href="https://fonts.googleapis.com/css2?family=Montserrat:wght@300;400;600&display=swap" rel="stylesheet">
<style>
  :root {
    --bg: #ececec;
    --bar: #141414;
    --screen: #f6f8f9;
    --row: #ffffff;
    --red: #f0362c;
    --yellow: #fbbb06;
    --blue: #0aa6ef;
    --green: #43a546;
    --ink: #1c1c1c;
    --muted: #a5a5a5;
    --bar-text: #9a9a9a;
  }
  * { box-sizing: border-box; margin: 0; padding: 0; }
  html, body { width: 1200px; height: 1095px; overflow: hidden; }
  body { background: var(--bg); font-family: "Montserrat", sans-serif; position: relative; }

  .app-screen {
    position: absolute; left: 300px; top: 47px; width: 600px; height: 1000px;
    background: var(--screen); display: flex; flex-direction: column;
    box-shadow: 0 10px 40px rgba(0,0,0,.12);
  }
  .title-bar {
    height: 70px; background: var(--bar); display: flex; align-items: center;
    justify-content: space-between; padding: 0 18px 0 22px;
  }
  .title-bar h1 { color: #fff; font-weight: 300; font-size: 24px; }
  .exit-button {
    background: var(--red); color: #fff; font-weight: 300; font-size: 20px;
    padding: 6px 26px;
  }

  .alert-list { display: flex; flex-direction: column; gap: 4px; padding: 6px 8px 0; }
  .alert-row { display: flex; align-items: center; height: 78px; background: var(--row); }
  .alert-icon { width: 78px; height: 78px; display: flex; align-items: center; justify-content: center; flex: none; }
  .alert-text { padding-left: 18px; font-weight: 300; font-size: 19px; }
  .is-red .alert-icon { background: var(--red); }  .is-red .alert-text { color: var(--red); }
  .is-yellow .alert-icon { background: var(--yellow); } .is-yellow .alert-text { color: var(--yellow); }
  .is-blue .alert-icon { background: var(--blue); } .is-blue .alert-text { color: var(--blue); }

  .road-info { text-align: center; padding-top: 22px; }
  .road-name { font-size: 24px; font-weight: 400; color: var(--ink); }
  .community-name { font-size: 17px; font-weight: 300; color: var(--muted); margin-top: 2px; }

  .speed-gauge { display: block; margin: 6px auto 0; }
  .gauge-label { font-family: "Montserrat", sans-serif; font-size: 20px; fill: var(--ink); text-anchor: middle; dominant-baseline: middle; }

  .action-strip { display: flex; align-items: flex-end; justify-content: space-between; padding: 0 8px; margin-top: auto; }
  .action-tile { width: 150px; height: 90px; display: flex; align-items: center; gap: 8px; padding: 0 10px; color: #fff; font-size: 14px; line-height: 1.15; font-weight: 400; }
  .report-camera { background: var(--blue); }
  .school-intimation { background: var(--yellow); align-self: flex-start; height: 80px; margin-bottom: 60px; }
  .current-speed {
    background: var(--red); color: #fff; font-weight: 600; font-size: 36px;
    padding: 14px 28px; margin-bottom: 18px;
  }

  .bottom-bar {
    height: 80px; background: var(--bar); display: flex; align-items: center;
    justify-content: space-between; padding: 0 22px; color: var(--bar-text); font-weight: 300; font-size: 22px;
  }
  .settings-link { display: flex; align-items: center; gap: 14px; color: #d8d8d8; }
</style>
</head>
<body>
<main class="app-screen">
  <header class="title-bar">
    <h1>Speed Limit</h1>
    <span class="exit-button">Exit</span>
  </header>

  <section class="alert-list">
    <div class="alert-row is-red">
      <div class="alert-icon">
        <svg width="54" height="54" viewBox="0 0 54 54"><circle cx="27" cy="27" r="24" fill="none" stroke="#fff" stroke-width="3"/><text x="27" y="28" fill="#fff" font-family="Montserrat, sans-serif" font-size="17" text-anchor="middle" dominant-baseline="middle">140</text></svg>
      </div>
      <p class="alert-text">The speed limit on this road is 140 Km/h.</p>
    </div>
    <div class="alert-row is-red">
      <div class="alert-icon">
        <svg width="54" height="54" viewBox="0 0 54 54"><circle cx="27" cy="27" r="24" fill="none" stroke="#fff" stroke-width="3"/><rect x="25" y="13" width="4" height="19" fill="#fff"/><circle cx="27" cy="39" r="2.6" fill="#fff"/></svg>
      </div>
      <p class="alert-text">You are at the limit of permissible speed.</p>
    </div>
    <div class="alert-row is-yellow">
      <div class="alert-icon">
        <svg width="54" height="54" viewBox="0 0 54 54" role="img" aria-label="School crossing sign"><circle cx="27" cy="27" r="24" fill="none" stroke="#fff" stroke-width="3"/><circle cx="27" cy="27" r="13" fill="#fff" opacity=".9"/></svg>
      </div>
      <p class="alert-text">School Zone 600m.</p>
    </div>
    <div class="alert-row is-blue">
      <div class="alert-icon">
        <svg width="54" height="54" viewBox="0 0 54 54"><circle cx="27" cy="27" r="24" fill="none" stroke="#fff" stroke-width="3"/><rect x="16" y="16" width="22" height="22" rx="2" fill="none" stroke="#fff" stroke-width="2.5"/><circle cx="25" cy="25" r="4" fill="none" stroke="#fff" stroke-width="2.5"/><rect x="19" y="32" width="16" height="3" fill="#fff"/></svg>
      </div>
      <p class="alert-text">Camera to 220m.</p>
    </div>
  </section>

  <section class="road-info">
    <h2 class="road-name">Al Noor Coastal Road</h2>
    <p class="community-name">Community Name</p>
  </section>

  <svg class="speed-gauge" width="380" height="336" viewBox="0 0 520 460">
    <path d="M132.7 387.3 A180 180 0 0 1 132.7 132.7" fill="none" stroke="var(--green)" stroke-width="14"/>
    <path d="M132.7 132.7 A180 180 0 0 1 387.3 132.7" fill="none" stroke="var(--yellow)" stroke-width="14"/>
    <path d="M387.3 132.7 A180 180 0 0 1 387.3 387.3" fill="none" stroke="var(--red)" stroke-width="14"/>
    <g stroke="var(--screen)" stroke-width="5">
      <line x1="95.8" y1="304" x2="72" y2="310.5"/>
      <line x1="95.8" y1="216" x2="72" y2="209.5"/>
      <line x1="216" y1="95.8" x2="209.5" y2="72"/>
      <line x1="304" y1="95.8" x2="310.5" y2="72"/>
      <line x1="424.2" y1="216" x2="448" y2="209.5"/>
      <line x1="424.2" y1="304" x2="448" y2="310.5"/>
    </g>
    <g class="gauge-label">
      <text class="gauge-label" x="108" y="418">0</text>
      <text class="gauge-label" x="46" y="318">20</text>
      <text class="gauge-label" x="46" y="202">40</text>
      <text class="gauge-label" x="100" y="100">60</text>
      <text class="gauge-label" x="202" y="44">80</text>
      <text class="gauge-label" x="318" y="44">100</text>
      <text class="gauge-label" x="422" y="100">120</text>
      <text class="gauge-label" x="478" y="202">140</text>
      <text class="gauge-label" x="478" y="318">160</text>
      <text class="gauge-label" x="422" y="420">180</text>
    </g>
    <polygon points="405,221 263.6,273.5 256.4,246.5" fill="var(--red)"/>
    <circle cx="260" cy="260" r="16" fill="var(--red)"/>
  </svg>

  <section class="action-strip">
    <div class="action-tile report-camera">
      <svg width="46" height="46" viewBox="0 0 54 54"><circle cx="27" cy="27" r="24" fill="none" stroke="#fff" stroke-width="3"/><rect x="16" y="16" width="22" height="22" rx="2" fill="none" stroke="#fff" stroke-width="2.5"/><circle cx="25" cy="25" r="4" fill="none" stroke="#fff" stroke-width="2.5"/><rect x="19" y="32" width="16" height="3" fill="#fff"/></svg>
      <span>Report<br>Camera</span>
    </div>
    <div class="current-speed">140 Km/h</div>
    <div class="action-tile school-intimation">
      <svg width="46" height="46" viewBox="0 0 54 54" role="img" aria-label="School crossing sign"><circle cx="27" cy="27" r="24" fill="none" stroke="#fff" stroke-width="3"/><circle cx="27" cy="27" r="13" fill="#fff" opacity=".9"/></svg>
      <span>School<br>Intimation</span>
    </div>
  </section>

  <footer class="bottom-bar">
    <span class="about-link">About</span>
    <span class="settings-link">Settings &amp; Controls
      <svg width="30" height="30" viewBox="0 0 30 30"><g fill="#fff"><circle cx="15" cy="15" r="10"/><rect x="13" y="1" width="4" height="28"/><rect x="1" y="13" width="28" height="4"/><rect x="13" y="1" width="4" height="28" transform="rotate(45 15 15)"/><rect x="13" y="1" width="4" height="28" transform="rotate(-45 15 15)"/></g><circle cx="15" cy="15" r="5" fill="var(--bar)"/></svg>
      <svg width="6" height="26" viewBox="0 0 6 26"><g fill="#fff"><circle cx="3" cy="3" r="2.6"/><circle cx="3" cy="13" r="2.6"/><circle cx="3" cy="23" r="2.6"/></g></svg>
    </span>
  </footer>
</main>
</body>
</html>
```